All-Natural Head Lice Removal company

I need a business card with my pre-existing logo. We are a new company located in Portland Oregon that goes into peoples homes to help with head lice removal. My products and approach are all- natural and also will be around children.On my current logo we used Teal Bl and the color Green. I am open to new ideas just want it simple and creative

Target Market(s)

my biggest market is families of school aged children

Industry/Entity Type

Business

Contact Information for Business Card

see upload for details from previous business card

Font styles to use
Serif

Colors
33a6d7
9bcb3b
f37122

Requirements
Must have
• Basic information/ logo put into a creative format that is catching to the eye
Nice to have
• creative

```html
<!DOCTYPE html>
<html lang="en">
<head>
<meta charset="utf-8">
<title>Nit Nook Business Card</title>
<link href="https://fonts.googleapis.com/css2?family=Open+Sans:wght@400;600;700;800&display=swap" rel="stylesheet">
<style>
  :root{
    --green:#76bc3a;
    --green-dark:#5ea22a;
    --blue:#33a6d7;
    --ink:#1e1e1e;
    --white:#ffffff;
    --paper:#f4f4f2;
    --backdrop:#e9e5dd;
  }
  *{box-sizing:border-box;margin:0;padding:0}
  html,body{width:1200px;height:1023px;overflow:hidden}
  body{background:var(--backdrop);font-family:"Open Sans",sans-serif;position:relative}

  .card{position:absolute;width:640px;height:366px;border-radius:26px;overflow:hidden;
        box-shadow:0 10px 28px rgba(0,0,0,.18)}

  /* Front */
  .card-front{left:70px;top:70px;background:linear-gradient(180deg,var(--white),var(--paper))}
  .brand{position:absolute;left:0;right:0;top:46px;display:flex;align-items:center;justify-content:center;gap:14px}
  .brand-dot{width:54px;height:54px;border-radius:50%;background:var(--green)}
  .brand-name{font-weight:800;font-size:40px;color:var(--ink);letter-spacing:.5px}
  .holder{position:absolute;left:0;right:0;top:122px;text-align:center}
  .holder-name{font-weight:800;font-size:24px;color:var(--green)}
  .holder-role{font-weight:800;font-size:14px;color:var(--ink);margin-top:2px}

  .contact-band{position:absolute;left:0;right:0;bottom:0;height:118px;background:var(--green)}
  .contact{position:absolute;top:-30px;width:200px;text-align:center;color:var(--white)}
  .contact.phone{left:14px}
  .contact.email{left:220px}
  .contact.web{left:426px}
  .icon{width:60px;height:60px;border-radius:50%;margin:0 auto;border:3px solid var(--white);
        display:flex;align-items:center;justify-content:center}
  .icon.phone{background:var(--green)}
  .icon.email{background:var(--ink)}
  .icon.web{background:var(--blue)}
  .contact-text{margin-top:22px;font-size:16px;letter-spacing:.2px}

  /* Back */
  .card-back{left:490px;top:590px;background:linear-gradient(160deg,var(--green-dark),var(--green))}
  .back-brand{position:absolute;left:0;right:0;top:64px;display:flex;align-items:center;justify-content:center;gap:16px}
  .back-brand .brand-dot{width:64px;height:64px;background:none;border:3px solid var(--ink)}
  .back-brand .brand-name{font-size:48px}
  .tagline{position:absolute;left:0;right:0;top:178px;text-align:center;color:var(--ink);font-size:19px;line-height:1.5}
  .tagline .site-key{color:var(--blue)}
</style>
</head>
<body>

<section class="card card-front">
  <div class="brand">
    <span class="brand-dot"></span>
    <span class="brand-name">Nit Nook</span>
  </div>
  <div class="holder">
    <div class="holder-name">Dana Whitfield</div>
    <div class="holder-role">Owner</div>
  </div>

  <div class="contact-band">
    <div class="contact phone">
      <div class="icon phone">
        <svg width="30" height="30" viewBox="0 0 24 24" fill="#fff"><path d="M6.6 10.8a15 15 0 0 0 6.6 6.6l2.2-2.2a1 1 0 0 1 1-.25 11.4 11.4 0 0 0 3.6.57 1 1 0 0 1 1 1V20a1 1 0 0 1-1 1A17 17 0 0 1 3 4a1 1 0 0 1 1-1h3.5a1 1 0 0 1 1 1c0 1.25.2 2.45.57 3.57a1 1 0 0 1-.25 1z"/></svg>
      </div>
      <div class="contact-text">1-555-010-NITS (6487)</div>
    </div>
    <div class="contact email">
      <div class="icon email">
        <svg width="32" height="24" viewBox="0 0 32 24" fill="none" stroke="#fff" stroke-width="2"><rect x="2" y="2" width="28" height="20"/><path d="M2 2l14 11L30 2"/></svg>
      </div>
      <div class="contact-text">hello@nitnook.com</div>
    </div>
    <div class="contact web">
      <div class="icon web">
        <svg width="30" height="30" viewBox="0 0 24 24" fill="none" stroke="#fff" stroke-width="1.6"><circle cx="12" cy="12" r="10"/><ellipse cx="12" cy="12" rx="4.5" ry="10"/><path d="M2 12h20M4 6.5h16M4 17.5h16"/></svg>
      </div>
      <div class="contact-text">www.nitnook.com</div>
    </div>
  </div>
</section>

<section class="card card-back">
  <div class="back-brand">
    <span class="brand-dot"></span>
    <span class="brand-name">Nit Nook</span>
  </div>
  <p class="tagline">
    Try Nit Nook Today and Be Lice Free Tomorrow!<br>
    All Natural In-Home Lice Removal Service<br>
    www.<span class="site-key">nitnook</span>.com
  </p>
</section>

</body>
</html>
```